REVISED : Logo & Stationery design for Naturopath

1. I need a logo and stationery (A4 letterhead, Business card & postcard size card for voucher/birthday/reminder use) for my new clinic. 
2. Overall look / logo needs to achieve: sense of personal attention (handwriting like script use somewhere), be unfussy, elegant, professional, modern. calm.
3. MUST be DIFFERENT to what we normally see for naturopaths.
4. Logo will be used eventually on new website so must lend itself to that use.
5. Possible tag lines 'Health is in your nature' or 'Health for generations' = general themes
6. Should appeal to men, mothers, women, depressed, families
Please feel free to submit logo designs prior to stationery work up if preferred.  

Thanks for your designs.  I have updated my brief a little, I hope that it now gives a clearer picture of what I'm looking for.  Have a great day! Marion

Hi Everyone.  I have uploaded some dandelion to give you an idea of the symmetry, perfection and airiness that I'm looking for.

heading away for a week, so apologies to extend the deadline.  Decision will be made on Friday.  Thanks for your patience.

My clients are aged from 5m to 75 years and have an array of problems. My main interest is joint and general inflammation and the role of genetic heritage and nutrigenomics. I follow an evidence based approach. Have a look at www.marionfeltwell.com.au

Consulting

1. some script based font 
2.  colours of nature . 
3. Trading Name: Marion Feltwell Naturopathy 
4. Company Name: Brisklane Motion Works Pty Ltd ABN: 58 219 307 614 (these must be on for legal reasons but not form part of logo or overall company name. 
5. Mailing Address: PO Box 4836, Wendaroo Flat NSW 2894 
6. Clinic Address: TBC 
7. Tel: 1300 48 29 05 
8. e: naturopathy@marionfeltwell.com.au 
9. w: marionfeltwell.com.au
Business Card and Postcard do not need ABN & Pty Ltd name.
Business Card should have my qualifications: Bachelor of Health Science (Complementary Medicine), ND.
1. design able to be embossed (card, business card)
2. able to be used on non-bleached recycled paper 
3. suitable of matt / uncoated card
4. good for vegetable dye printing
5. concept I really like is of a dandelion blowing in the wind (themes = herb, wistful, dissemination of information, free and easy) 
6. also really like idea of a 'tree of life'
7. but your interpretation of something entirely different might be a winner
8. Use of either of the tag lines 
9. Monochromatic 
1. photos
2. more than 3 colours
3. Leaves (too much like every other Naturopath)

```html
<!DOCTYPE html>
<html lang="en">
<head>
<meta charset="utf-8">
<title>Marion Feltwell Naturopathy – Stationery</title>
<link rel="stylesheet" href="https://fonts.googleapis.com/css2?family=Pinyon+Script&family=Roboto+Condensed:wght@300&family=Arimo&display=swap">
<style>
  :root {
    --paper: #ffffff;
    --ink-frame: #111111;
    --brand-green: #445f2e;
    --brand-brown: #5b3a1d;
    --rule-grey: #a99c98;
    --stamp-grey: #8a8a8a;
    --caption: #111111;
  }
  * { box-sizing: border-box; margin: 0; padding: 0; }
  html, body { width: 927px; height: 1200px; overflow: hidden; background: var(--paper); }
  .sheet { position: relative; width: 927px; height: 1200px; }

  .piece { position: absolute; background: var(--paper); }
  .piece--black { border: 1.5px solid var(--ink-frame); }
  .piece--green { border: 1.5px solid var(--brand-green); }

  .mark { position: absolute; display: block; }
  .mark circle { fill: var(--brand-green); }

  .wordmark {
    position: absolute;
    font-family: "Pinyon Script", cursive;
    color: var(--brand-brown);
    white-space: nowrap;
    line-height: 1;
  }
  .script { font-family: "Pinyon Script", cursive; line-height: 1; white-space: nowrap; position: absolute; }
  .details {
    position: absolute;
    font-family: "Roboto Condensed", sans-serif;
    font-weight: 300;
    color: var(--brand-brown);
    white-space: nowrap;
  }

  /* business card front */
  .bc-front { left: 91px; top: 55px; width: 379px; height: 216px; }
  .bc-front .mark { left: 22px; top: 14px; }
  .bc-front .wordmark { left: 130px; top: 152px; font-size: 19px; }

  /* postcard front */
  .pc-front { left: 505px; top: 55px; width: 325px; height: 227px; }
  .pc-front .mark { left: 103px; top: 24px; }
  .pc-front .wordmark { left: 0; right: 0; top: 175px; text-align: center; font-size: 14px; }

  /* business card back */
  .bc-back { left: 91px; top: 320px; width: 379px; height: 217px; }
  .bc-back .script { color: var(--brand-brown); }
  .appt-title { left: 19px; top: 20px; font-size: 20px; }
  .field-label { left: 20px; font-size: 14px; }
  .field-rule { position: absolute; height: 0; border-top: 0.8px solid var(--rule-grey); }
  .bc-back .details { right: 22px; top: 140px; text-align: right; font-size: 10px; line-height: 12.6px; }

  /* postcard back */
  .pc-back { left: 505px; top: 309px; width: 325px; height: 228px; }
  .tagline { left: 13px; top: 14px; font-size: 14px; color: var(--brand-green); }
  .stamp-box { position: absolute; left: 273px; top: 16px; width: 36px; height: 42px; border: 0.8px solid var(--stamp-grey); }
  .pc-back .details { left: 0; right: 0; top: 165px; text-align: center; font-size: 6.2px; line-height: 8.7px; }

  /* letterhead */
  .letterhead { left: 91px; top: 595px; width: 414px; height: 536px; }
  .letterhead .mark { left: 157px; top: 24px; }
  .letterhead .wordmark { left: 0; right: 0; top: 140px; text-align: center; font-size: 16px; }
  .letterhead .details { left: 0; right: 0; top: 466px; text-align: center; font-size: 5px; line-height: 6.6px; }

  /* master logo */
  .logo-lockup { position: absolute; left: 530px; top: 594px; width: 310px; }
  .logo-lockup .mark { left: 40px; top: 0; }
  .logo-lockup .wordmark { left: 0; right: 0; top: 308px; text-align: center; font-size: 31px; }

  .caption {
    position: absolute; left: 569px; top: 1016px;
    font-family: "Arimo", Arial, sans-serif;
    font-size: 21.5px; line-height: 27.5px; color: var(--caption);
  }
</style>
</head>
<body>
<main class="sheet">

  <section class="piece piece--black bc-front" aria-label="Business card front">
    <svg class="mark" width="160" height="160" viewBox="0 0 160 160" aria-hidden="true"><circle cx="80" cy="80" r="70"/></svg>
    <p class="wordmark">Marion Feltwell Naturopathy</p>
  </section>

  <section class="piece piece--green pc-front" aria-label="Postcard front">
    <svg class="mark" width="120" height="120" viewBox="0 0 120 120" aria-hidden="true"><circle cx="60" cy="60" r="54"/></svg>
    <p class="wordmark">Marion Feltwell Naturopathy</p>
  </section>

  <section class="piece piece--black bc-back" aria-label="Business card back">
    <p class="script appt-title">Your next appointment is</p>
    <p class="script field-label" style="top:58px">on</p>
    <span class="field-rule" style="left:38px;width:320px;top:71px"></span>
    <p class="script field-label" style="top:96px">at</p>
    <span class="field-rule" style="left:38px;width:320px;top:111px"></span>
    <p class="script field-label" style="left:18px;top:133px">notes</p>
    <span class="field-rule" style="left:52px;width:145px;top:145px"></span>
    <span class="field-rule" style="left:18px;width:179px;top:180px"></span>
    <span class="field-rule" style="left:18px;width:161px;top:184px"></span>
    <address class="details" style="font-style:normal">
      Brisklane Motion Works Pty Ltd<br>
      Clinic Address<br>
      1(800)482-2905<br>
      naturopathy@marionfeltwell.com.au<br>
      marionfeltwell.com.au
    </address>
  </section>

  <section class="piece piece--green pc-back" aria-label="Postcard back">
    <p class="script tagline">Health is in your nature</p>
    <span class="stamp-box"></span>
    <address class="details" style="font-style:normal">
      Brisklane Motion Works Pty Ltd<br>
      Mailing Address: PO Box 4836, Wendaroo Flat NSW 2894<br>
      Clinic Address<br>
      1(800)482-2905<br>
      naturopathy@marionfeltwell.com.au, marionfeltwell.com.au<br>
      ABN: 58 219 307 614
    </address>
  </section>

  <section class="piece piece--black letterhead" aria-label="A4 letterhead">
    <svg class="mark" width="100" height="100" viewBox="0 0 100 100" aria-hidden="true"><circle cx="50" cy="50" r="46"/></svg>
    <p class="wordmark">Marion Feltwell Naturopathy</p>
    <address class="details" style="font-style:normal">
      Brisklane Motion Works Pty Ltd<br>
      Mailing Address: PO Box 4836, Wendaroo Flat NSW 2894<br>
      Clinic Address<br>
      1(800)482-2905<br>
      naturopathy@marionfeltwell.com.au<br>
      marionfeltwell.com.au<br>
      ABN: 58 219 307 614
    </address>
  </section>

  <section class="logo-lockup" aria-label="Logo">
    <svg class="mark" width="230" height="230" viewBox="0 0 230 230" aria-hidden="true"><circle cx="115" cy="115" r="110"/></svg>
    <p class="wordmark">Marion Feltwell Naturopathy</p>
  </section>

  <p class="caption">From top right corner:<br>Business card front and<br>back,postcard front and back<br>letterhead and logo.</p>

</main>
</body>
</html>
```